Eye catching business card

2 sided
Black background with logo in color on one side along with the words "Proudly serving the commercial and defense industries since 1975"
2nd side to contain contact information (see attached current business card) and "Waterjet, Composite, Precision Machining and Clean Room Manufacturing" with a very faint watermark of a waving USA Flag in the back ground.
Remove the "est. 195" from the current logo design

```html
<!DOCTYPE html>
<html lang="en">
<head>
<meta charset="utf-8">
<title>Vanguard Fabrication Inc – Business Card</title>
<link rel="stylesheet" href="https://fonts.googleapis.com/css2?family=Lato:wght@400;700&display=swap">
<style>
  :root {
    --backdrop: #4b2f1e;
    --card-dark: #2b2b2c;
    --card-light: #ffffff;
    --brand-blue: #3381d0;
    --text-gray: #6a6a6a;
    --name-gray: #9a9a9a;
    --rule-blue: #3d86cf;
    --watermark-cool: #eef0f7;
    --watermark-warm: #fbf3f1;
  }
  * { margin: 0; padding: 0; box-sizing: border-box; }
  html, body { width: 1200px; height: 848px; overflow: hidden; }
  body {
    position: relative;
    background: var(--backdrop);
    font-family: "Lato", sans-serif;
  }
  .card {
    position: absolute;
    box-shadow: 0 6px 14px rgba(0,0,0,0.45);
    overflow: hidden;
  }
  /* Front */
  .card-front {
    left: 251px; top: 28px; width: 672px; height: 380px;
    background: var(--card-dark);
  }
  .brand-mark {
    position: absolute; left: 50%; top: 118px; transform: translateX(-50%);
    display: flex; flex-direction: column; align-items: center; gap: 22px; white-space: nowrap;
  }
  .brand-dot {
    width: 64px; height: 64px; border-radius: 50%;
    background: var(--brand-blue);
  }
  .brand-name {
    font-weight: 700; font-size: 30px; letter-spacing: 1px; line-height: 1;
    color: var(--name-gray);
  }
  .front-tagline {
    position: absolute; left: 0; right: 0; top: 323px;
    text-align: center; font-size: 18px; color: var(--brand-blue);
  }
  /* Back */
  .card-back {
    left: 249px; top: 441px; width: 677px; height: 375px;
    background: var(--card-light);
  }
  .flag-watermark {
    position: absolute; inset: 0;
    background: linear-gradient(120deg, var(--watermark-cool) 0%, var(--watermark-warm) 55%, var(--card-light) 100%);
  }
  .back-brand {
    position: absolute; left: 217px; top: 190px; transform: translate(-50%, -50%);
    display: flex; flex-direction: column; align-items: center; gap: 16px; white-space: nowrap;
  }
  .back-brand .brand-dot { width: 56px; height: 56px; }
  .back-brand .brand-name { font-size: 20px; color: #8a8a8a; letter-spacing: 0.5px; }
  .divider {
    position: absolute; left: 357px; top: 99px; width: 2px; height: 180px;
    background: var(--rule-blue);
  }
  .contact {
    position: absolute; left: 379px; top: 92px;
    color: var(--text-gray); font-size: 17px; line-height: 1.35;
  }
  .contact-name { color: var(--brand-blue); font-weight: 700; font-size: 21px; line-height: 1.1; }
  .contact-title { margin-bottom: 14px; }
  .contact-address { margin-bottom: 14px; }
  .contact-line { display: flex; align-items: center; gap: 7px; line-height: 1.3; }
  .contact-line svg { width: 12px; height: 12px; fill: var(--brand-blue); flex: none; }
  .contact-line .accent { color: var(--brand-blue); }
  .services {
    position: absolute; left: 0; right: 0; top: 323px;
    text-align: center; font-size: 18px; color: var(--text-gray);
  }
</style>
</head>
<body>
  <section class="card card-front">
    <div class="brand-mark">
      <span class="brand-dot"></span>
      <span class="brand-name">Vanguard Fabrication Inc</span>
    </div>
    <p class="front-tagline">Proudly serving the commercial and defense industries since 1975"</p>
  </section>

  <section class="card card-back">
    <div class="flag-watermark" role="img" aria-label="Very faint waving USA flag watermark in the background"></div>
    <div class="back-brand">
      <span class="brand-dot"></span>
      <span class="brand-name">Vanguard Fabrication Inc</span>
    </div>
    <div class="divider"></div>
    <div class="contact">
      <div class="contact-name">Daniel Reyes</div>
      <div class="contact-title">President</div>
      <div class="contact-address">214 Harbor Street, 3rd Floor<br>Newport, RI 02840</div>
      <div class="contact-line">
        <svg viewBox="0 0 24 24"><path d="M6.6 10.8a15 15 0 0 0 6.6 6.6l2.2-2.2a1 1 0 0 1 1-.25 11.4 11.4 0 0 0 3.6.57 1 1 0 0 1 1 1V20a1 1 0 0 1-1 1A17 17 0 0 1 3 4a1 1 0 0 1 1-1h3.5a1 1 0 0 1 1 1c0 1.25.2 2.45.57 3.57a1 1 0 0 1-.25 1z"/></svg>
        <span>555.204.7718</span>
      </div>
      <div class="contact-line">
        <svg viewBox="0 0 24 24"><path d="M2 5h20v14H2z M2 5l10 8 10-8" /></svg>
        <span>hello@northpinestudio.com</span>
      </div>
      <div class="contact-line">
        <svg viewBox="0 0 24 24"><path d="M12 2a10 10 0 1 0 0 20 10 10 0 0 0 0-20zm0 2c.9 1.2 1.6 2.8 1.9 5h-3.8c.3-2.2 1-3.8 1.9-5zM4.3 11h3.8c.1 1.5.3 2.9.8 4H5.2a8 8 0 0 1-.9-4zm5.8 0h3.8c-.1 1.5-.4 2.9-.9 4h-2c-.5-1.1-.8-2.5-.9-4zm5.8 0h3.8a8 8 0 0 1-.9 4h-3.7c.5-1.1.7-2.5.8-4z"/></svg>
        <span>www.<span class="accent">vanguardfab</span>.com</span>
      </div>
    </div>
    <p class="services">Waterjet, Composite, Precision Machining and Clean Room Manufacturing</p>
  </section>
</body>
</html>
```